依頼詳細
<現状サイトの課題>
①一目で、何をしている会社なのかが分からない。
⇒商品画像・作業画像などを入れ、分かりやすく目を引き付けるようにする。

②項目が小さく、引き付けにくいデザイン。
⇒アイコンを大きくして、デザイン性を持たせる。

③自社の強みを視覚化できていない。
⇒図や写真を追加し、視覚的に伝わるようにする。

④自社の新着情報がないので社内の動きが把握できない。
⇒新着ニュースを追加し社内の動きが把握できるようにする。

⑤企業規模が小さく感じてしまう。
⇒洗練されたデザイン、コンテンツの充実、グローバルサイトの作成により企業規模をワンランク大きく見えるように表現する。
----------------------------------
<現在のサイト>
明確なサイトの情報共有はできませんが、TOPページの情報を一部伏せて共有します。添付の”TOPページ”をご参照ください。

<サイトリニューアルの方針>
①強みを明確にする為、全体的に画像化し打ち出したい。TOPページは動画を掲載し、よりリアルにユーザー様にイメージが伝わるデザインにする。

②企業規模をワンランク大きく見えるように表現し、グローバル化についてもアピールすることで、事業規模の大きい信頼出来る会社であることが分かるようにし、新規顧客の獲得および定着するようにサイトリニューアルを行う。

③必須機能
・TOPページへ動画を埋め込む。
・スマホ対応(レスポンシブウェブデザイン)にする。
・ウェブ見積り機能を設け、いつでも見積りが確認できるようにする。(TOPページにバナーを設けるなどデザインする)

<イメージ参考サイト>
①メインカラーをブルーとし、TOPページを開くとすぐに大きな画像イメージが見えます。
https://www.e-hariwa.co.jp/

②トップページに表示される、動画イメージです。
https://www.dovel.co.jp/

③コンテンツの配置や施工事例が見やすいです。
http://www.tasemi-kk.com/

④TOPページに施工写真や文字が挿入されており分かりやすい。また企業イメージがよく考えられており、ブランディングされています。
http://www.fujiyaga.co.jp/

<カラーテーマ>
①青系(堅実・信頼・クール)または水色系(さわやか・清潔感)

②青4割、白6割の配色のイメージでお願いします。制作の際は、カラーチャート(カラーを選んだ理由)もご提示いただけると幸いです。

<重視する点/検討基準>
①サイトコンセプトにあったデザイン(ご提案の際は、制作頂いたデザインコンセプト及びデザイン説明コメントの記載をお願い致します)

②納期厳守

<具体的な制作数>
TOPページ:1ページ(PC版のデザイン制作をお願いします)

<選考の進め方>
ご提案頂いたデザイン内容・コンセプトなどをもとに、プロジェクトメンバーで選考、決定致します。
※今回は、トップページデザインのみの見積りとなります。
今後、コーディングを依頼する可能性もございます。その場合は改めてクリエタスを通じてご依頼させて頂きます。パララックスデザインでのコーディングも条件として入れてまいります。
1ページ
青系、水色系
• イラストレーター形式 (.ai)
• フォトショップ形式 (.psd)
追記です。
サイトコンセプトの資料も添付いたします。
宜しくお願いいたします。

クライアント様と協議させていただき、コンセプトに合った総合的なデザインを評価させて頂きました。
その中で、クライアント様からの評価が多かった「Pixfern様」を当選とさせていただきました。ありがとうございました。

ランサーの皆さん、このように沢山の素敵なデザインをご提案頂き本当にありがとうございました。
コンセプトを基に、クライアント様とも大いに悩んで決定させて頂きました。
また、選定が期限間近になってしまいましたこと、申し訳ございませんでした。

機会があれば、今後ともどうぞ宜しくお願い致します。

```html
<!DOCTYPE html>
<html lang="ja">
<head>
<meta charset="utf-8">
<title>KANAE STEEL | 鉄製品の製造・加工</title>
<link rel="stylesheet" href="https://fonts.googleapis.com/css2?family=Noto+Sans+JP:wght@400;500;700;900&family=Roboto:wght@400;700;900&display=swap">
<style>
:root{
  --blue:#0fa3e6;
  --blue-dark:#0a7fc0;
  --navy:#1d3a5c;
  --text:#333;
  --muted:#777;
  --line:#e2e2e2;
  --gray-bg:#f2f3f5;
  --footer-bg:#eef0f3;
  --white:#fff;
}
*{box-sizing:border-box;margin:0;padding:0}
html,body{width:1200px;height:3988px;overflow:hidden}
body{font-family:"Noto Sans JP",sans-serif;color:var(--text);background:var(--white);font-size:14px;line-height:1.6}
a{color:inherit;text-decoration:none}

/* top bar */
.topbar{height:48px;display:flex;justify-content:space-between;align-items:center;padding-left:100px}
.topbar-note{font-size:11px;color:var(--muted)}
.topbar-estimate{width:340px;height:48px;margin-right:100px;background:var(--blue);color:#fff;display:flex;align-items:center;justify-content:center;gap:12px;font-size:15px;font-weight:700}
.topbar-estimate .arrow{margin-left:24px}

/* header */
.site-header{height:120px;display:flex;align-items:center;justify-content:space-between;padding:0 100px}
.brand{display:flex;align-items:center;gap:10px;white-space:nowrap}
.brand-square{width:16px;height:16px;background:var(--navy);flex:none}
.brand-name{font-family:"Noto Sans JP",sans-serif;font-weight:700;font-size:28px;color:var(--navy);line-height:1;letter-spacing:.04em;white-space:nowrap}
.global-nav{display:flex}
.global-nav a{width:112px;height:100px;display:flex;flex-direction:column;align-items:center;justify-content:center;gap:8px;font-size:13px;font-weight:700;border-left:1px solid var(--line);white-space:nowrap}
.global-nav a:last-child{border-right:1px solid var(--line)}
.global-nav svg{width:30px;height:30px}

/* hero */
.hero{position:relative;height:492px}
.hero-visual{position:absolute;inset:0;background:linear-gradient(100deg,#4d5a66 0%,#7d8893 40%,#a7adb3 70%,#5f6a74 100%)}
.hero-content{position:absolute;left:100px;top:232px;color:#fff}
.hero-title{font-size:40px;font-weight:900;letter-spacing:.05em;text-shadow:0 2px 6px rgba(0,0,0,.4)}
.hero-lead{display:inline-block;margin-top:10px;background:rgba(0,0,0,.55);padding:4px 14px;font-size:14px;font-weight:500}
.hero-btn{margin-top:40px;width:390px;height:62px;border:2px solid #fff;background:rgba(0,0,0,.35);display:flex;align-items:center;padding:0 24px;gap:20px;font-size:18px;font-weight:700;color:#fff}
.hero-btn .arrow{margin-left:auto}

/* section commons */
.section{text-align:center}
.section-label{display:inline-block;border:1px solid var(--blue);color:var(--blue);font-family:"Roboto",sans-serif;font-size:12px;font-weight:700;letter-spacing:.1em;padding:3px 20px;background:#fff}
.section-title{font-size:38px;font-weight:900;margin-top:12px;letter-spacing:.05em}
.section-title::after{content:"";display:block;width:40px;height:3px;background:var(--blue);margin:12px auto 0}
.more-btn{display:flex;align-items:center;justify-content:center;width:400px;height:60px;margin:0 auto;background:var(--blue);color:#fff;font-size:14px;font-weight:700;position:relative}
.more-btn .arrow{position:absolute;right:24px}

/* strengths */
.strengths{height:800px;padding-top:72px}
.strength-list{display:flex;justify-content:space-between;width:1000px;margin:48px auto 0}
.strength{width:290px}
.strength-icon{width:160px;height:160px;border-radius:50%;background:var(--blue);margin:0 auto;display:flex;align-items:center;justify-content:center}
.strength-icon svg{width:84px;height:84px}
.strength-sub{margin-top:20px;font-size:17px;font-weight:700}
.strength-main{font-size:24px;font-weight:900;color:var(--blue);line-height:1.3}
.strength-text{margin-top:22px;text-align:left;font-size:13px;line-height:1.9;color:#555}
.strengths .more-btn{margin-top:48px}

/* works */
.works{height:800px;background:var(--gray-bg);padding-top:68px;position:relative}
.work-list{display:flex;gap:24px;width:1000px;margin:44px auto 0}
.work-card{width:232px;background:#fff;text-align:left}
.work-photo{height:200px}
.work-body{padding:14px 14px 18px}
.work-title{color:var(--blue);font-weight:700;font-size:14px}
.work-text{font-size:12px;color:#555;margin-top:6px;line-height:1.7}
.works .more-btn{margin-top:52px}
.works .slider-prev{position:absolute;left:48px;top:370px}
.works .slider-next{position:absolute;right:48px;top:370px}

/* news */
.news{height:820px;padding-top:32px}
.news-list{width:1000px;margin:50px auto 0;text-align:left}
.news-item{display:flex;gap:24px;padding:20px 0;border-bottom:1px dashed #ccc}
.news-thumb{width:120px;height:100px;flex:none}
.news-date{font-size:12px;color:var(--muted)}
.news-title{font-size:18px;font-weight:700;margin:2px 0 6px}
.news-text{font-size:13px;color:#555;line-height:1.8}
.news-text .more{color:var(--blue);text-decoration:underline;margin-left:6px}
.news .more-btn{margin-top:48px}

/* estimate band */
.estimate-band{height:160px;background:var(--blue);display:flex;align-items:center;justify-content:center}
.estimate-box{width:600px;height:80px;background:#fff;display:flex;align-items:center;padding:0 40px;gap:60px;font-size:24px;font-weight:900;color:var(--navy)}
.estimate-box .arrow{margin-left:auto}

/* banners */
.banners{height:240px;display:flex;gap:20px;padding:40px 100px 0}
.banner{width:320px;height:160px;position:relative;border:1px solid var(--line)}
.banner-visual{position:absolute;inset:0;background:linear-gradient(90deg,#fff 0%,#fff 35%,#b9c6d3 60%,#7e8fa2 100%)}
.banner-text{position:absolute;left:22px;top:46px}
.banner-en{font-family:"Roboto",sans-serif;font-size:10px;color:var(--blue);letter-spacing:.1em}
.banner-ja{font-size:22px;font-weight:900;color:var(--navy);border-bottom:2px solid var(--blue)}

/* footer */
.site-footer{height:460px;background:var(--footer-bg);padding:40px 100px 0;position:relative}
.footer-nav{display:flex;gap:34px}
.footer-col{width:172px}
.footer-col h3{font-size:13px;font-weight:700;display:flex;align-items:center;gap:6px}
.footer-col h3::before{content:"";width:8px;height:8px;background:var(--blue)}
.footer-col ul{list-style:none;margin:6px 0 0 14px}
.footer-col li{font-size:12px;color:#555;line-height:2}
.footer-col li::before{content:"・"}
.footer-group{margin-top:24px}
.footer-brand{position:absolute;left:0;right:0;top:330px;display:flex;flex-direction:column;align-items:center}
.footer-brand .brand-name{font-size:22px}
.footer-address{font-size:11px;color:#555;line-height:1.6;margin-top:8px;text-align:center}
.copyright{height:48px;background:var(--blue);color:#fff;font-size:11px;display:flex;align-items:center;justify-content:center}
</style>
</head>
<body>

<div class="topbar">
  <p class="topbar-note">鉄製品の設計・製造・加工なら「KANAE STEEL」へ。高品質と短納期でお応えします。</p>
  <a class="topbar-estimate" href="#">
    <svg width="22" height="22" viewBox="0 0 24 24" fill="none" stroke="#fff" stroke-width="2"><rect x="4" y="2" width="16" height="20" rx="2"/><line x1="7" y1="6" x2="17" y2="6"/><circle cx="8" cy="11" r=".8" fill="#fff"/><circle cx="12" cy="11" r=".8" fill="#fff"/><circle cx="16" cy="11" r=".8" fill="#fff"/><circle cx="8" cy="15" r=".8" fill="#fff"/><circle cx="12" cy="15" r=".8" fill="#fff"/><circle cx="16" cy="15" r=".8" fill="#fff"/></svg>
    ウェブ見積りはこちら<span class="arrow">›</span>
  </a>
</div>

<header class="site-header">
  <div class="brand">
    <span class="brand-square"></span>
    <span class="brand-name">KANAE STEEL</span>
  </div>
  <nav class="global-nav">
    <a href="#"><svg viewBox="0 0 24 24" fill="none" stroke="#0fa3e6" stroke-width="2"><rect x="4" y="3" width="16" height="18"/><line x1="8" y1="7" x2="16" y2="7"/><line x1="8" y1="11" x2="16" y2="11"/><line x1="8" y1="15" x2="16" y2="15"/></svg>会社概要</a>
    <a href="#"><svg viewBox="0 0 24 24" fill="none" stroke="#0fa3e6" stroke-width="2"><rect x="3" y="7" width="18" height="13"/><path d="M9 7V4h6v3"/></svg>事業案内</a>
    <a href="#"><svg viewBox="0 0 24 24" fill="none" stroke="#0fa3e6" stroke-width="2"><path d="M14 4l6 6-10 10H4v-6z"/></svg>技術情報</a>
    <a href="#"><svg viewBox="0 0 24 24" fill="none" stroke="#0fa3e6" stroke-width="2"><circle cx="9" cy="8" r="3"/><circle cx="16" cy="9" r="2.5"/><path d="M3 20c0-4 3-6 6-6s6 2 6 6M15 14c3 0 6 2 6 6"/></svg>スタッフ紹介</a>
    <a href="#"><svg viewBox="0 0 24 24" fill="none" stroke="#0fa3e6" stroke-width="2"><rect x="3" y="4" width="18" height="16"/><line x1="7" y1="9" x2="17" y2="9"/><line x1="7" y1="13" x2="14" y2="13"/></svg>社内報</a>
    <a href="#"><svg viewBox="0 0 24 24" fill="none" stroke="#0fa3e6" stroke-width="2"><path d="M4 20l2-6 10-10 4 4-10 10z"/></svg>ブログ</a>
    <a href="#"><svg viewBox="0 0 24 24" fill="none" stroke="#0fa3e6" stroke-width="2"><rect x="3" y="5" width="18" height="14"/><path d="M3 6l9 7 9-7"/></svg>お問い合わせ</a>
  </nav>
</header>

<section class="hero">
  <div class="hero-visual" role="img" aria-label="鉄製品の加工現場と作業風景の写真"></div>
  <div class="hero-content">
    <h1 class="hero-title">クオリティーの高い鉄製品を、創造する。</h1>
    <p class="hero-lead">高いサービスを提供するため、培ってきた技術とネットワークを強みに「高品質・短納期」を実現</p>
    <a class="hero-btn" href="#">
      <svg width="30" height="30" viewBox="0 0 24 24" fill="none" stroke="#fff" stroke-width="2"><rect x="4" y="2" width="16" height="20" rx="2"/><line x1="7" y1="6" x2="17" y2="6"/><line x1="8" y1="11" x2="16" y2="11"/><line x1="8" y1="15" x2="16" y2="15"/></svg>
      ウェブ見積りはこちら<span class="arrow">›</span>
    </a>
  </div>
</section>

<section class="section strengths">
  <span class="section-label">3 STRENGTHS</span>
  <h2 class="section-title">3つの強み</h2>
  <div class="strength-list">
    <div class="strength">
      <div class="strength-icon"><svg viewBox="0 0 24 24" fill="none" stroke="#fff" stroke-width="1.8"><path d="M14 6a4 4 0 0 0 5 5l-9 9-3-3 9-9"/><path d="M4 4l6 6M4 4l2-1 1 2"/></svg></div>
      <p class="strength-sub">ご満足いただける</p>
      <p class="strength-main">高品質・短納期サービス</p>
      <p class="strength-text">長年培った加工技術と徹底した品質管理により、高品質な鉄製品を短い納期でお届けします。急なご依頼にも柔軟に対応できる生産体制を整えています。</p>
    </div>
    <div class="strength">
      <div class="strength-icon"><svg viewBox="0 0 24 24" fill="none" stroke="#fff" stroke-width="1.8"><circle cx="12" cy="10" r="5"/><path d="M5 10a7 7 0 0 1 14 0M5 10v3h2v-3M19 10v3h-2M6 21c1-3 3-4 6-4s5 1 6 4"/></svg></div>
      <p class="strength-sub">なんでもご相談いただける</p>
      <p class="strength-main">柔軟な体制</p>
      <p class="strength-text">設計から製造、施工までを一貫して承ります。小さなご相談から大型案件まで、経験豊富なスタッフが丁寧にヒアリングし最適なご提案をいたします。</p>
    </div>
    <div class="strength">
      <div class="strength-icon"><svg viewBox="0 0 24 24" fill="none" stroke="#fff" stroke-width="1.8"><path d="M2 10l4-4 4 2 4-2 4 0 4 4-4 4-5 5-3-3-4-2z"/><path d="M10 8l3 3"/></svg></div>
      <p class="strength-sub">常に拡張し続ける</p>
      <p class="strength-main">お客様目線の姿勢</p>
      <p class="strength-text">お客様の声を大切に、常にサービスの改善と拡張に取り組んでいます。国内外のネットワークを活かし、信頼されるパートナーを目指します。</p>
    </div>
  </div>
  <a class="more-btn" href="#">事業案内を見る<span class="arrow">›</span></a>
</section>

<section class="section works">
  <span class="section-label">WORKS</span>
  <h2 class="section-title">施工事例</h2>
  <svg class="slider-prev" width="20" height="40" viewBox="0 0 20 40"><path d="M16 4L4 20l12 16" fill="none" stroke="#bbb" stroke-width="3"/></svg>
  <svg class="slider-next" width="20" height="40" viewBox="0 0 20 40"><path d="M4 4l12 16L4 36" fill="none" stroke="#bbb" stroke-width="3"/></svg>
  <div class="work-list">
    <article class="work-card"><div class="work-photo" role="img" aria-label="鉄骨建築の施工写真" style="background:linear-gradient(160deg,#c9d3dc,#6f8092)"></div><div class="work-body"><p class="work-title">企業名が入ります</p><p class="work-text">施工内容の概要が入ります。施工内容の概要が入ります。</p></div></article>
    <article class="work-card"><div class="work-photo" role="img" aria-label="鉄骨の骨組み工事の施工写真" style="background:linear-gradient(160deg,#d8c8b5,#7a5f4c)"></div><div class="work-body"><p class="work-title">企業名が入ります</p><p class="work-text">施工内容の概要が入ります。施工内容の概要が入ります。</p></div></article>
    <article class="work-card"><div class="work-photo" role="img" aria-label="完成した屋内空間の施工写真" style="background:linear-gradient(160deg,#eef0ef,#b8bdb6)"></div><div class="work-body"><p class="work-title">企業名が入ります</p><p class="work-text">施工内容の概要が入ります。施工内容の概要が入ります。</p></div></article>
    <article class="work-card"><div class="work-photo" role="img" aria-label="建設中の高層建築の施工写真" style="background:linear-gradient(160deg,#c9b99a,#6b6a5a)"></div><div class="work-body"><p class="work-title">企業名が入ります</p><p class="work-text">施工内容の概要が入ります。施工内容の概要が入ります。</p></div></article>
  </div>
  <a class="more-btn" href="#">施工事例一覧を見る<span class="arrow">›</span></a>
</section>

<section class="section news">
  <span class="section-label">NEWS</span>
  <h2 class="section-title">新着情報</h2>
  <div class="news-list">
    <article class="news-item"><div class="news-thumb" role="img" aria-label="ニュースのサムネイル写真" style="background:linear-gradient(160deg,#b8c4a8,#5d6e4e)"></div><div><p class="news-date">2016.06.00</p><h3 class="news-title">タイトルが入りますタイトルが入ります</h3><p class="news-text">お知らせの本文が入ります。お知らせの本文が入ります。お知らせの本文が入ります。お知らせの本文が入ります。お知らせの本文が入ります。<span class="more">続きを読む</span></p></div></article>
    <article class="news-item"><div class="news-thumb" role="img" aria-label="ニュースのサムネイル写真" style="background:linear-gradient(160deg,#d4b8a8,#7a4e44)"></div><div><p class="news-date">2016.06.00</p><h3 class="news-title">タイトルが入りますタイトルが入ります</h3><p class="news-text">お知らせの本文が入ります。お知らせの本文が入ります。お知らせの本文が入ります。お知らせの本文が入ります。お知らせの本文が入ります。<span class="more">続きを読む</span></p></div></article>
    <article class="news-item"><div class="news-thumb" role="img" aria-label="ニュースのサムネイル写真" style="background:linear-gradient(160deg,#c5ccd4,#6b7580)"></div><div><p class="news-date">2016.06.00</p><h3 class="news-title">タイトルが入りますタイトルが入ります</h3><p class="news-text">お知らせの本文が入ります。お知らせの本文が入ります。お知らせの本文が入ります。お知らせの本文が入ります。お知らせの本文が入ります。<span class="more">続きを読む</span></p></div></article>
  </div>
  <a class="more-btn" href="#">新着情報一覧を見る<span class="arrow">›</span></a>
</section>

<section class="estimate-band">
  <a class="estimate-box" href="#">
    <svg width="44" height="44" viewBox="0 0 24 24" fill="none" stroke="#0fa3e6" stroke-width="2"><rect x="4" y="2" width="16" height="20" rx="2"/><line x1="7" y1="6" x2="17" y2="6"/><line x1="8" y1="11" x2="16" y2="11"/><line x1="8" y1="15" x2="16" y2="15"/></svg>
    ウェブ見積りはこちら<span class="arrow">›</span>
  </a>
</section>

<section class="banners">
  <a class="banner" href="#"><div class="banner-visual" role="img" aria-label="社員の集合写真"></div><div class="banner-text"><p class="banner-en">RECRUIT</p><p class="banner-ja">採用情報</p></div></a>
  <a class="banner" href="#"><div class="banner-visual" role="img" aria-label="スタッフの写真"></div><div class="banner-text"><p class="banner-en">STAFF</p><p class="banner-ja">スタッフ紹介</p></div></a>
  <a class="banner" href="#"><div class="banner-visual" role="img" aria-label="社内の様子の写真"></div><div class="banner-text"><p class="banner-en">IN-HOUSE</p><p class="banner-ja">社内報</p></div></a>
</section>

<footer class="site-footer">
  <div class="footer-nav">
    <div class="footer-col"><h3>ホーム</h3></div>
    <div class="footer-col"><h3>会社概要</h3><ul><li>ご挨拶</li><li>アクセスマップ</li><li>取引先</li><li>沿革</li><li>会社の特徴</li></ul>
      <div class="footer-group"><h3>グループ会社</h3><ul><li>グループ一覧</li><li>アクセスマップ</li></ul></div></div>
    <div class="footer-col"><h3>事業案内</h3><ul><li>クオリティへの取組</li><li>設備紹介</li><li>加工実績</li></ul></div>
    <div class="footer-col"><h3>採用情報</h3><ul><li>人材育成</li><li>先輩の声</li><li>募集要項</li><li>年間スケジュール</li></ul></div>
    <div class="footer-col"><h3>スタッフ紹介</h3><ul><li>社内報</li><li>ブログ</li><li>お問い合わせ</li></ul></div>
  </div>
  <div class="footer-brand">
    <div class="brand">
      <span class="brand-square"></span>
      <span class="brand-name">KANAE STEEL</span>
    </div>
    <p class="footer-address">〒000-0000<br>架空県架空市中央0-0-0<br>TEL 000-000-0000</p>
  </div>
</footer>
<div class="copyright">Copyright (c) KANAE STEEL All rights reserved.</div>

</body>
</html>
```